Full Stationary
Business Cards & Stationery for Limo Service - Transportation
Business Cards & Stationery for Limo Service
Professional
Glen Harbury / Dale Pronto
President / General Manager
1187 Fenwick Blvd, Suite 300 Des Moines, IA 50317
844.RQT.CARZ
info@vantregocars.example
www.vantregocars.example
I don't want this card to be too cluttered but I want it to look super sharp and modern. I like modern font however I want it to remain similar to the logo and professional as we are handing these cards to operators throughout the United States.
Be creative. I am unsure of the future demand for QR codes. I have attached 3, one for the website, Facebook, and Twitter. Feel free to use them if you wish, however, if there is something new I am unaware of please feel free to use this new technology. As stated earlier, I am unsure how well these work in todays world versus a few years ago. I have used them previously on the backs of business cards and think it looks cool, however if I am mistaken of something different please let me know.

```html
<!DOCTYPE html>
<html lang="en">
<head>
<meta charset="utf-8">
<title>Vantrego Cars – Business Card</title>
<link href="https://fonts.googleapis.com/css2?family=Montserrat:wght@400&display=swap" rel="stylesheet">
<style>
  :root {
    --backdrop: #3b3b3d;
    --card-white: #ffffff;
    --ink: #3a3a3c;
    --ink-soft: #6b6b6e;
    --grey-light: #d6d6d8;
    --grey-mid: #9a9a9d;
    --grey-dark: #5c5c60;
    --swoosh: #111113;
    --on-grey: #ffffff;
  }
  * { margin: 0; padding: 0; box-sizing: border-box; }
  html, body {
    width: 1200px; height: 653px; overflow: hidden;
    background: var(--backdrop);
    font-family: "Montserrat", sans-serif;
  }
  .stage {
    position: relative; width: 1200px; height: 653px;
    display: flex; justify-content: center; align-items: center; gap: 60px;
  }
  .card {
    position: relative; width: 520px; height: 297px;
    background: var(--card-white); overflow: hidden;
  }
  .brand { display: flex; align-items: center; gap: 12px; color: var(--ink); font-weight: 400; }
  .brand-mark { width: 34px; height: 34px; background: var(--ink); flex: none; }
  .brand-name { display: flex; flex-direction: column; line-height: 1; }
  .brand-name .primary { font-size: 30px; letter-spacing: 3px; }
  .brand-name .secondary { font-size: 11px; letter-spacing: 7.5px; margin-top: 5px; }

  .card-front .brand {
    position: absolute; left: 50%; top: 50%; transform: translate(-50%, -50%);
  }

  .card-back .backdrop-shape { position: absolute; inset: 0; }
  .card-back .brand { position: absolute; left: 172px; top: 30px; gap: 9px; }
  .card-back .brand-mark { width: 24px; height: 24px; }
  .card-back .brand-name .primary { font-size: 18px; letter-spacing: 1.5px; }
  .card-back .brand-name .secondary { font-size: 7px; letter-spacing: 4.6px; margin-top: 3px; }

  .contact {
    position: absolute; right: 16px; top: 32px; width: 138px;
    list-style: none; color: var(--ink-soft); font-size: 7px; line-height: 1.3;
  }
  .contact li { display: flex; justify-content: space-between; align-items: center; gap: 6px; margin-bottom: 6px; white-space: nowrap; }
  .contact .address { display: block; margin-bottom: 10px; }
  .contact svg { width: 8px; height: 8px; flex: none; fill: var(--ink-soft); }
  .contact .icon-mail { fill: none; stroke: var(--ink-soft); stroke-width: 1; }

  .holder { position: absolute; left: 40px; bottom: 38px; color: var(--on-grey); }
  .holder .name { font-size: 13px; letter-spacing: 1.5px; text-transform: uppercase; }
  .holder .role { font-size: 8px; letter-spacing: 1px; margin-top: 4px; }
</style>
</head>
<body>
<main class="stage">
  <section class="card card-front">
    <div class="brand">
      <span class="brand-mark"></span>
      <span class="brand-name"><span class="primary">VANTREGO</span><span class="secondary">CARS</span></span>
    </div>
  </section>

  <section class="card card-back">
    <svg class="backdrop-shape" viewBox="0 0 520 297" preserveAspectRatio="none" aria-hidden="true">
      <defs>
        <linearGradient id="grey-sweep" x1="0" y1="0" x2="1" y2="1">
          <stop offset="0" stop-color="var(--grey-light)"/>
          <stop offset="0.5" stop-color="var(--grey-mid)"/>
          <stop offset="1" stop-color="var(--grey-dark)"/>
        </linearGradient>
      </defs>
      <path d="M0,0 L150,0 C92,62 185,150 520,166 L520,297 L0,297 Z" fill="url(#grey-sweep)"/>
      <path d="M166,0 C100,62 195,146 520,156 L520,168 C178,160 78,72 146,0 Z" fill="var(--swoosh)"/>
      <path d="M140,0 C70,74 170,170 520,178" fill="none" stroke="var(--card-white)" stroke-width="1.2"/>
    </svg>

    <div class="brand">
      <span class="brand-mark"></span>
      <span class="brand-name"><span class="primary">VANTREGO</span><span class="secondary">CARS</span></span>
    </div>

    <ul class="contact">
      <li class="address">1187 Fenwick Blvd, Suite 300<br>Des Moines, IA 50317</li>
      <li><span>844.RQT.CARZ</span>
        <svg viewBox="0 0 10 10"><path d="M2,0.5 L4,2.5 L3,4 C3.8,5.6 4.5,6.3 6,7 L7.5,6 L9.5,8 L8,9.5 C4,9 1,6 0.5,2 Z"/></svg></li>
      <li><span>info@vantregocars.example</span>
        <svg viewBox="0 0 10 10" class="icon-mail"><path d="M0.5,2 H9.5 V8 H0.5 Z M1,2.5 L5,5.5 L9,2.5"/></svg></li>
      <li><span>www.vantregocars.example</span>
        <svg viewBox="0 0 10 10"><circle cx="5" cy="5" r="4.5"/></svg></li>
    </ul>

    <div class="holder">
      <p class="name">Glen Harbury</p>
      <p class="role">President</p>
    </div>
  </section>
</main>
</body>
</html>
```